Business card design and logo for plumbing bussiness

We are wanting a logo for a plumbing business is Queensland Australia. KRV Plumbing and Drainage will be doing works on domestic and commercial sites.
Plumbing, drainage and gas works. We are wanting something that will stand out and be noticed. Colours could be black blue and white but open for suggestions.

Target Market(s)

Builders and home renovators

Industry/Entity Type

Plumbing

Contact Information for Business Card

Miles Dorgan - Director
0417 582 913
miles@krvplumbing.example.com.au
QBCC: 847 2106
ABN: 52 319 407 281

Font styles to use
Sans Serif

Colors
000000

Requirements
Must have
• Clear defined branding

```html
<!DOCTYPE html>
<html lang="en">
<head>
<meta charset="utf-8">
<title>KRV Plumbing and Drainage – Business Card</title>
<link rel="stylesheet" href="https://fonts.googleapis.com/css2?family=Open+Sans:wght@400;600;700&display=swap">
<style>
  :root {
    --backdrop: #5a3f2d;
    --card: #050505;
    --brand-blue: #3a8fd9;
    --text-white: #ffffff;
  }
  * { margin: 0; padding: 0; box-sizing: border-box; }
  html, body {
    width: 1200px;
    height: 1000px;
    overflow: hidden;
    background: var(--backdrop);
    font-family: "Open Sans", Arial, sans-serif;
  }
  .canvas {
    position: relative;
    width: 1200px;
    height: 1000px;
  }
  .card {
    position: absolute;
    left: 266px;
    width: 666px;
    height: 398px;
    background: var(--card);
    color: var(--text-white);
  }
  .card--front { top: 73px; }
  .card--back { top: 533px; }

  .brand {
    position: absolute;
    display: flex;
    align-items: center;
    gap: 14px;
    color: var(--brand-blue);
    font-weight: 600;
    white-space: nowrap;
  }
  .brand__dot {
    flex: none;
    border-radius: 50%;
    background: var(--brand-blue);
  }
  .card--front .brand {
    left: 34px;
    top: 92px;
    font-size: 29px;
  }
  .card--front .brand__dot { width: 22px; height: 22px; }
  .card--back .brand {
    left: 0;
    right: 0;
    top: 160px;
    justify-content: center;
    font-size: 35px;
  }
  .card--back .brand__dot { width: 26px; height: 26px; }

  .credentials {
    position: absolute;
    left: 33px;
    top: 234px;
    font-size: 17px;
    line-height: 26px;
  }
  .credentials .label { color: var(--brand-blue); font-weight: 600; }

  .contact {
    position: absolute;
    left: 33px;
    top: 297px;
    font-size: 17px;
    line-height: 28px;
    list-style: none;
  }
  .contact li { display: flex; align-items: center; gap: 12px; }
  .contact svg { width: 15px; height: 12px; fill: var(--brand-blue); flex: none; }

  .person {
    position: absolute;
    right: 33px;
    top: 213px;
    text-align: right;
  }
  .person__name {
    color: var(--brand-blue);
    font-weight: 700;
    font-size: 21px;
    letter-spacing: 0.3px;
    line-height: 30px;
  }
  .person__role { font-size: 16px; line-height: 22px; }

  .services {
    position: absolute;
    left: 0;
    right: 0;
    top: 346px;
    text-align: center;
    font-size: 17px;
  }
</style>
</head>
<body>
<main class="canvas">
  <section class="card card--front" aria-label="Business card front">
    <div class="brand"><span class="brand__dot"></span>KRV Plumbing and Drainage</div>

    <div class="credentials">
      <p><span class="label">QBCC:</span> 847 2106</p>
      <p><span class="label">ABN:</span> 52 319 407 281</p>
    </div>

    <ul class="contact">
      <li>
        <svg viewBox="0 0 15 12" aria-hidden="true"><path d="M1 4 Q7.5 -1 14 4 L12 5.5 L10.5 3.5 L4.5 3.5 L3 5.5 Z M3.5 6 L11.5 6 L13 11 L2 11 Z"/></svg>
        0417 582 913
      </li>
      <li>
        <svg viewBox="0 0 15 12" aria-hidden="true"><path d="M0 1 L15 1 L7.5 7 Z M0 2.5 L7.5 8.5 L15 2.5 L15 11 L0 11 Z"/></svg>
        miles@krvplumbing.example.com.au
      </li>
    </ul>

    <div class="person">
      <p class="person__name">MILES DORGAN</p>
      <p class="person__role">Director</p>
    </div>
  </section>

  <section class="card card--back" aria-label="Business card back">
    <div class="brand"><span class="brand__dot"></span>KRV Plumbing and Drainage</div>
    <p class="services">Plumbing | Drainage | Gas</p>
  </section>
</main>
</body>
</html>
```